Asia based real estate financing firm needs and AWESOME design for a biz card -Harbor Lending Circle

Looking for a stylish, & corporate-looking business card for a real estate financing brokerage firm in Asia, offering global mortgage loans. I uploaded our current logos. We would like to add a splash of color (perhaps the house icon) or any other suggestions are open. For the winning designer, we have a lot of work! Thanks and best of luck!

Target Market(s)

Real estate investors globally. We want to look more like a BANK and NOT a real estate company. Please don't play up on a "house" design.

Industry/Entity Type

Banking

Contact Information for Business Card

Harbor Lending Circle
Peter Wilks
Co-Founder | Partner

14 Cassia Lane, Suite 310
Singapore 047219
www.hlc-example.asia
peterwilks@hlc-example.asia
+65 555-0142
WeChat: peterwilks

Colors

Designer to choose colors to be used in the design.

Requirements
Must have
• Must have the standard business requirements for a card; name, address, email, etc
• Can be horizontal or vertical.
Nice to have
• It would be great to see some sort of variation to the logo with a pop of color. Red is good as we're in Asia, however, other options work as well.
• Our tag line is - Borderless mortgages. It doesn't have to be on the card but might be nice.
• I'd like to start seeing our tagline within the cards as well. - Borderless mortgages.
• Also, please add our location. The location for this card is Singapore so perhaps it can be highlighted or emphasised in some way.
• Singapore | Hong Kong | Shanghai | Manila
• As we will soon open an office in Shanghai, having an option for both languages would be great.
Should not have
• I'm exceited and open to your creativity ... knock it out of the park!

```html
<!DOCTYPE html>
<html lang="en">
<head>
<meta charset="utf-8">
<title>Harbor Lending Circle – Business Card</title>
<link rel="stylesheet" href="https://fonts.googleapis.com/css2?family=Cinzel:wght@500&family=Work+Sans:wght@400;500&display=swap">
<style>
  :root {
    --backdrop: #1a1a1b;
    --card: #232324;
    --card-edge: #2e2e30;
    --ink: #f4f4f4;
    --ink-soft: #dcdcdc;
    --accent: #2f6fd1;
  }
  * { margin: 0; padding: 0; box-sizing: border-box; }
  html, body { width: 1200px; height: 900px; overflow: hidden; }
  body {
    background: var(--backdrop);
    display: flex;
    flex-direction: column;
    align-items: center;
    justify-content: center;
    gap: 40px;
    font-family: "Work Sans", sans-serif;
  }
  .card {
    width: 660px;
    height: 377px;
    background: linear-gradient(135deg, var(--card) 0%, var(--card-edge) 70%, var(--card) 100%);
    position: relative;
    box-shadow: 0 18px 40px rgba(0,0,0,.55);
  }
  .wordmark {
    font-family: "Cinzel", serif;
    font-weight: 500;
    color: var(--ink);
    letter-spacing: .06em;
    line-height: 1.15;
    text-align: center;
  }
  .card--front {
    display: flex;
    align-items: center;
    justify-content: center;
  }
  .card--front .wordmark { font-size: 40px; }
  .card--back {
    display: grid;
    grid-template-columns: 1fr 2px 1fr;
    align-items: center;
    padding: 0 34px;
  }
  .card--back .wordmark { font-size: 30px; padding-right: 26px; }
  .divider {
    width: 2px;
    height: 240px;
    background: var(--accent);
  }
  .contact { padding-left: 34px; color: var(--ink-soft); }
  .contact__name {
    color: var(--accent);
    font-size: 30px;
    font-weight: 500;
    letter-spacing: .06em;
    text-transform: uppercase;
    line-height: 1;
  }
  .contact__role { font-size: 14px; letter-spacing: .05em; margin-top: 6px; }
  .contact__address { font-size: 14px; letter-spacing: .04em; line-height: 1.45; margin-top: 16px; }
  .contact__list { list-style: none; margin-top: 14px; font-size: 14px; letter-spacing: .03em; }
  .contact__list li { display: flex; align-items: center; gap: 9px; line-height: 1.6; }
  .contact__list svg { width: 12px; height: 12px; flex: none; }
</style>
</head>
<body>
  <section class="card card--front">
    <div class="wordmark">Harbor Lending<br>Circle</div>
  </section>

  <section class="card card--back">
    <div class="wordmark">Harbor Lending<br>Circle</div>
    <div class="divider"></div>
    <div class="contact">
      <div class="contact__name">Peter Wilks</div>
      <div class="contact__role">Co-Founder | Partner</div>
      <div class="contact__address">14 Cassia Lane, Suite 310<br>Singapore 047219</div>
      <ul class="contact__list">
        <li>
          <svg viewBox="0 0 12 12" aria-hidden="true"><path d="M2.5 1h2l1 2.5-1.2 1a6 6 0 0 0 3.2 3.2l1-1.2 2.5 1v2c0 .5-.5 1-1 1A9 9 0 0 1 1.5 2c0-.5.5-1 1-1z" fill="var(--accent)"/></svg>
          +65 555-0142
        </li>
        <li>
          <svg viewBox="0 0 12 12" aria-hidden="true"><rect x="1" y="2.5" width="10" height="7" fill="none" stroke="var(--accent)" stroke-width="1.2"/><path d="M1 2.5l5 4 5-4" fill="none" stroke="var(--accent)" stroke-width="1.2"/></svg>
          peterwilks@hlc-example.asia
        </li>
        <li>
          <svg viewBox="0 0 12 12" aria-hidden="true"><g fill="none" stroke="var(--accent)" stroke-width="1"><circle cx="6" cy="6" r="5"/><ellipse cx="6" cy="6" rx="2.2" ry="5"/><path d="M1 6h10M2 3.5h8M2 8.5h8"/></g></svg>
          www.hlc-example.asia
        </li>
        <li>
          <svg viewBox="0 0 12 12" aria-hidden="true"><circle cx="6" cy="6" r="5" fill="var(--accent)"/></svg>
          peterwilks
        </li>
      </ul>
    </div>
  </section>
</body>
</html>
```